Medical centre needs a business card

We are a medcial centre in Australia, needing a new business card. Our demographic is low working class families. We are going to be renovating our premises to modernise the look and also had a new logo done a few months ago representing quality and community, and now need to update our cards. It needs to be doubled sided, with logo and contact details on the front, and appointment details on the back. . Needs to be modern and simple, easy to read. <br/><br/>Name: Kindle Grove Medical Centre <br/>Address: 512 Larkin Rd (Cnr Larkin Rd & Fenwick Vale Rd),<br/>Tamsworth Court Shopping Centre, Paralowie, SA 5108<br/>Ph: 08 8193 4067<br/>Tag line: Where your care comes first<br/>Website: www.kindlegrovemedicalexample.com.au<br/>Online bookings also available<br/><br/>(On the back, to have 3 lines of appointments that can be written in.<br/>Day, date, time)<br/><br/>Your next appointment is on<br/>Can try “M T W Th F Sa Su _________________ at ____________ am/pm” or other combinations <br/>Please advise as soon as possible if unable to attend<br/>Cancellation fees apply if less than 2 hrs notice<br/>Online appointments available (please highlight this option by either by position, colour or font)

Target Market(s)

Lower social economic working class, young families to seniors

Industry/Entity Type

Medical Centre

Contact Information for Business Card

Kindle Grove Medical Centre
512 Larkin Rd (Cnr Larkin Rd & Fenwick Vale Drive)
Tamsworth Court Shopping Centre
Brayfield SA 5190
Ph: 08 8193 4067
www.kindlegrovemedicalexample.com.au
Tagline line: where your care comes first
Back side is for appointments
Your next appointment is with Dr ______________
Day/date/time (Please give 3 lines of appointments)
Please advise as soon as possible if unable to attend
Cancellation fees apply if less than 2 hours notice
Online appointments available
Book online easily and conveniently (please highlight online appointments)

Font styles to use
Serif
Sans Serif

Colors

Designer to choose colors to be used in the design.

Requirements
Must have
• Modern and simple
• Easy to ready
• Induces a wellbeing feeling
• Incorporate our logo colours and feel from logo
• Induces feeling of stability and security
Nice to have
• Attract attention
• Pleasant to look at
• Feeling of innovation
Should not have
• Loud clashing colours
• Overly luxurious feeling
• Overly artistic

```html
<!DOCTYPE html>
<html lang="en">
<head>
<meta charset="utf-8">
<title>Kindle Grove Medical Centre – Business Card</title>
<link href="https://fonts.googleapis.com/css2?family=Roboto:wght@400;500;700;900&family=Oswald:wght@500;600&display=swap" rel="stylesheet">
<style>
  :root {
    --bg: #e6e8eb;
    --card: #ffffff;
    --blue: #1f73c4;
    --blue-light: #3aa0e0;
    --blue-deep: #1562ad;
    --green: #8cc63f;
    --ink: #4a4f55;
    --rule: #9aa3ad;
    --wash: #eef5fc;
  }
  * { box-sizing: border-box; margin: 0; padding: 0; }
  html, body { width: 1200px; height: 960px; overflow: hidden; }
  body {
    background: var(--bg);
    font-family: "Roboto", Arial, sans-serif;
    display: flex;
    flex-direction: column;
    align-items: center;
    justify-content: center;
    gap: 28px;
  }
  .card {
    position: relative;
    width: 780px;
    height: 440px;
    background: var(--card);
    border-radius: 28px;
    overflow: hidden;
    box-shadow: 0 6px 18px rgba(0,0,0,.12);
  }

  /* Back: appointments */
  .appt { padding: 34px 56px 0; color: var(--blue); }
  .appt__mark {
    position: absolute; left: 50%; top: 50%;
    width: 300px; height: 300px; margin: -160px 0 0 -150px;
    border-radius: 50%; background: var(--wash);
  }
  .appt > *:not(.appt__mark) { position: relative; }
  .appt__title {
    text-align: center; font-weight: 500; font-size: 24px;
    letter-spacing: .04em; margin-bottom: 24px;
  }
  .appt__row { display: flex; align-items: flex-end; gap: 10px; margin-bottom: 22px; }
  .appt__label { font-weight: 500; font-size: 16px; text-transform: uppercase; white-space: nowrap; }
  .appt__line { flex: 1; border-bottom: 1.5px dotted var(--rule); height: 18px; }
  .appt__unit { font-size: 15px; }
  .appt__blank { border-bottom: 1.5px dotted var(--rule); height: 18px; margin-bottom: 22px; }
  .appt__note {
    text-align: center; color: var(--ink); font-size: 15px; line-height: 1.4;
    margin: 6px 0 16px;
  }
  .appt__cta {
    display: block; width: fit-content; margin: 0 auto;
    background: var(--blue); color: #fff; font-weight: 700; font-size: 17px;
    text-transform: uppercase; padding: 10px 28px; border-radius: 24px;
  }

  /* Front: identity and contact */
  .front__shape { position: absolute; inset: 0; }
  .brand {
    position: absolute; left: 54px; top: 120px; width: 340px;
    display: flex; align-items: center; gap: 14px;
  }
  .brand__dot { width: 34px; height: 34px; border-radius: 50%; background: var(--green); flex: none; }
  .brand__name {
    color: var(--blue); font-weight: 700; font-size: 27px; line-height: 1.15;
    text-transform: uppercase;
  }
  .person { position: absolute; left: 44px; top: 245px; width: 340px; text-align: center; }
  .person__name {
    font-family: "Oswald", "Arial Narrow", sans-serif; font-weight: 600;
    color: var(--blue); font-size: 40px; letter-spacing: .01em; text-transform: uppercase;
  }
  .person__role {
    font-family: "Oswald", "Arial Narrow", sans-serif; font-weight: 500;
    color: var(--green); font-size: 28px; text-transform: uppercase; margin-top: -4px;
  }
  .contact {
    position: absolute; right: 36px; top: 64px; width: 290px;
    color: #fff; text-align: right; font-size: 14.5px; line-height: 1.45; font-style: normal;
  }
  .contact__org { font-weight: 700; font-size: 15.5px; }
  .contact__item { display: flex; justify-content: flex-end; align-items: center; gap: 8px; margin-top: 10px; font-size: 14px; }
  .contact__item svg { width: 14px; height: 14px; flex: none; }
  .contact__tagline {
    margin-top: 30px; font-weight: 700; font-size: 16px; text-transform: uppercase;
  }
</style>
</head>
<body>

<section class="card appt" aria-label="Appointment card, back">
  <div class="appt__mark" aria-hidden="true"></div>
  <h2 class="appt__title">APPOINTMENTS</h2>
  <div class="appt__row">
    <span class="appt__label">Your next appointment is with Dr :</span>
    <span class="appt__line"></span>
  </div>
  <div class="appt__row">
    <span class="appt__label">Day :</span><span class="appt__line"></span>
    <span class="appt__label">Date :</span><span class="appt__line"></span>
    <span class="appt__label">Time :</span><span class="appt__line"></span>
    <span class="appt__unit">AM/PM</span>
  </div>
  <div class="appt__blank"></div>
  <div class="appt__blank"></div>
  <div class="appt__blank"></div>
  <p class="appt__note">Please advise as soon as possible if unable to attend Cancellation fees<br>apply if less than 2 hours notice Online appointments available</p>
  <span class="appt__cta">Book online easily &amp; conveniently</span>
</section>

<section class="card front" aria-label="Business card, front">
  <svg class="front__shape" viewBox="0 0 780 440" aria-hidden="true">
    <defs>
      <linearGradient id="panelFill" x1="0" y1="0" x2="1" y2="1">
        <stop offset="0" stop-color="#2f90d8"/>
        <stop offset="1" stop-color="#1562ad"/>
      </linearGradient>
    </defs>
    <path d="M 500 0 C 400 110, 390 320, 500 440" fill="none" stroke="#8cc63f" stroke-width="8"/>
    <path d="M 520 0 C 420 110, 412 320, 528 440 L 780 440 L 780 0 Z" fill="url(#panelFill)"/>
  </svg>

  <div class="brand">
    <span class="brand__dot" aria-hidden="true"></span>
    <span class="brand__name">Kindle Grove<br>Medical Centre</span>
  </div>

  <div class="person">
    <div class="person__name">Daniel Harrow</div>
    <div class="person__role">President</div>
  </div>

  <address class="contact">
    <div class="contact__org">Kindle Grove Medical Centre</div>
    <div>512 Larkin Rd</div>
    <div>(Cnr Larkin Rd &amp; Fenwick Vale Drive)</div>
    <div>Tamsworth Court Shopping Centre</div>
    <div>Brayfield SA 5190</div>
    <div class="contact__item">08 8193 4067
      <svg viewBox="0 0 24 24" fill="#fff" aria-hidden="true"><path d="M6.6 10.8a15.1 15.1 0 0 0 6.6 6.6l2.2-2.2c.3-.3.7-.4 1-.2 1.1.4 2.3.6 3.6.6.6 0 1 .4 1 1V20c0 .6-.4 1-1 1A17 17 0 0 1 3 4c0-.6.4-1 1-1h3.5c.6 0 1 .4 1 1 0 1.3.2 2.5.6 3.6.1.3 0 .7-.2 1z"/></svg>
    </div>
    <div class="contact__item">kindlegrovemedicalexample.com.au
      <svg viewBox="0 0 24 24" aria-hidden="true"><circle cx="12" cy="12" r="10" fill="#fff"/><path d="M2 12h20M12 2c3 3 3 17 0 20M12 2c-3 3-3 17 0 20" stroke="#1f73c4" stroke-width="1.6" fill="none"/></svg>
    </div>
    <div class="contact__tagline">Where your care comes first</div>
  </address>
</section>

</body>
</html>
```